| サイズ | A4 |
| ページ数 | 両面 |
| ▽ターゲット 上記の参加対象者向けのフライヤーです。30歳未満の若者(大学生など)が主なターゲットです。 ▽サイズ A4サイズ・両面を想定しています。 ▽参考 参考URL:http://www.kiriyama-shien.jp/sangyo/shoko/young-woman-bc-koubo.html |
どの提案も素敵でしたが、桐山県と協議の上、今回ご提案いただいたものに決定いたしました。
ご提案いただきました皆様、この度はご提案いただき、誠にありがとうございました。
どのご提案も本当に素敵なものばかりで、一つに絞るのが本当に難しかったのですが、桐山県さんと協議させていただき、ご提案いただいたものから一つを選ばせていただきました。
今後もクラウドソーシングサービスを活用していきたいと考えておりますので、是非今後とも、何卒よろしくお願い申し上げます。

```html
<!DOCTYPE html>
<html lang="ja">
<head>
<meta charset="utf-8">
<title>桐山県 若者・女性 起業チャレンジブートキャンプ</title>
<link href="https://fonts.googleapis.com/css2?family=Noto+Sans+JP:wght@400;700;900&family=Oswald:wght@500;700&display=swap" rel="stylesheet">
<style>
  :root{
    --blue:#1f5fa8;
    --blue-deep:#164a86;
    --ink:#1a1a1a;
    --red:#e0281e;
    --white:#ffffff;
    --grey:#555;
    --photo-top-a:#dfe6d9;
    --photo-top-b:#8fa388;
    --sky-a:#cfe6f6;
    --sky-b:#5aa3dc;
  }
  *{margin:0;padding:0;box-sizing:border-box}
  html,body{width:848px;height:1200px;overflow:hidden;background:var(--white)}
  body{font-family:"Noto Sans JP",sans-serif;color:var(--ink)}
  .flyer{position:relative;width:848px;height:1200px;overflow:hidden;background:var(--white)}

  .hero-photo{position:absolute;left:0;top:0;width:848px;height:500px;
    background:linear-gradient(100deg,#f7f8f4 0%,#f7f8f4 22%,var(--photo-top-a) 40%,var(--photo-top-b) 78%,#6f8468 100%)}
  .hero-fade{position:absolute;left:0;top:390px;width:848px;height:115px;
    background:linear-gradient(180deg,rgba(255,255,255,0) 0%,#fff 100%)}

  .badge{position:absolute;left:50px;top:38px;width:150px;height:150px;border-radius:50%;
    background:var(--blue);color:var(--white);display:flex;align-items:center;justify-content:center;
    text-align:center;font-weight:700;font-size:20px;line-height:1.35}

  .title{position:absolute;left:110px;top:245px;color:var(--blue);font-weight:900;
    font-size:38px;line-height:1.3;letter-spacing:1px}

  .headline{position:absolute;left:0;width:848px;text-align:center;font-family:"Oswald",sans-serif;
    font-weight:700;color:var(--ink);font-size:124px;line-height:1;letter-spacing:6px}
  .headline.line1{top:470px}
  .headline.line2{top:588px}

  .free-tag{position:absolute;left:640px;top:722px;width:160px;height:40px;background:var(--white);
    border:3px solid var(--red);color:var(--red);font-weight:900;font-size:24px;
    display:flex;align-items:center;justify-content:center;letter-spacing:2px}

  .date{position:absolute;left:55px;top:718px;width:400px;height:100px;color:var(--blue);font-family:"Oswald",sans-serif;font-weight:700}
  .date .year{position:absolute;left:0;top:0;font-size:24px;line-height:1}
  .date .main{position:absolute;left:0;top:24px;font-size:72px;line-height:1;white-space:nowrap;display:flex;align-items:flex-end}
  .date .day{display:inline-flex;flex-direction:column;font-size:18px;line-height:1.1;margin:0 8px 8px 6px}
  .date .arrow{font-size:32px;margin:0 6px 16px 0}

  .sky-photo{position:absolute;left:470px;top:770px;width:378px;height:345px;
    background:linear-gradient(180deg,var(--sky-b) 0%,var(--sky-a) 100%)}

  .pitch{position:absolute;left:600px;top:785px;color:var(--blue-deep);font-weight:900;font-size:24px;line-height:1.35;
    background:rgba(255,255,255,.88);padding:8px 12px}

  .details{position:absolute;left:55px;top:835px;width:400px;font-size:13px;line-height:1.45;color:var(--ink)}
  .details .row{display:flex;gap:8px;margin-bottom:10px}
  .details .label{flex:none;background:var(--blue);color:var(--white);font-weight:700;font-size:12px;padding:1px 6px;height:19px}
  .details .venue{font-size:17px;font-weight:700}
  .details .note{font-size:11px;color:var(--grey)}

  .footer{position:absolute;left:0;top:1120px;width:848px;height:80px;display:flex;align-items:center;padding:0 40px;gap:30px}
  .organizer{display:flex;align-items:center;gap:8px;font-weight:700;color:var(--blue);font-size:26px;white-space:nowrap}
  .organizer small{font-size:16px;color:var(--ink)}
  .organizer .mark{width:20px;height:20px;background:var(--blue);border-radius:50%}
  .contact{font-size:11px;line-height:1.5;color:var(--grey)}
</style>
</head>
<body>
<div class="flyer">
  <div class="hero-photo" role="img" aria-label="カフェのテラスでノートを広げて笑顔で話し合う若い男女の写真"></div>
  <div class="hero-fade"></div>

  <div class="badge">若者と女性<br>のための<br>起業実践研修</div>

  <h1 class="title">桐山県 若者・女性<br>起業チャレンジ<br>ブートキャンプ</h1>

  <div class="headline line1">CHALLENGE</div>
  <div class="headline line2">BOOT CAMP</div>

  <div class="sky-photo" role="img" aria-label="青空の下でジャンプするスーツ姿の男性の写真"></div>
  <div class="free-tag">参加無料</div>

  <div class="date">
    <span class="year">2015</span>
    <div class="main">8/21<span class="day"><span>FRI</span><span>13:00</span></span><span class="arrow">▶</span>23<span class="day"><span>SUN</span><span>12:00</span></span></div>
  </div>

  <p class="pitch">知りたいことが<br>詰まってる！<br>3日間の短期集中<br>プログラム</p>

  <div class="details">
    <div class="row"><span class="label">会場</span><div><span class="venue">桐山創業テクノロジーセンター</span><br><span class="note">桐山県北浜郡若葉村大字中央1-2</span></div></div>
    <div class="row"><span class="label">参加資格</span><div>桐山県内での起業を志している若者（30歳未満）及び女性<br><span class="note">※桐山県内で起業を目指す方であれば、県外在住者も可</span></div></div>
    <div class="row"><span class="label">募集人員</span><div>定員25名</div></div>
    <div class="row"><span class="label">参加費</span><div>無料 <span class="note">（ただし、宿泊費として3,000円をお支払いください）</span></div></div>
  </div>

  <footer class="footer">
    <div class="organizer"><small>主催：</small><span class="mark"></span>桐山県</div>
    <div class="contact">お申込み方法や詳細は桐山県のホームページをご覧ください。<br>http://www.kiriyama-shien.jp/sangyo/shoko/27kiriyama-bootcamp.html</div>
  </footer>
</div>
</body>
</html>
```